Ferris Contracting LLC Business Card Design

I am looking for a creative and unique business card design. We are a commercial construction general contractor. With the name "FERRIS" Contracting, I am hoping to see some neat designs that correlate with the name.

```html
<!DOCTYPE html>
<html lang="en">
<head>
<meta charset="utf-8">
<title>Ferris Contracting LLC – Business Card</title>
<link rel="stylesheet" href="https://fonts.googleapis.com/css2?family=Montserrat:wght@500;700;800&display=swap">
<style>
  :root {
    --backdrop: #2a2b2e;
    --card-dark: #222326;
    --card-edge: #1f86d4;
    --brand-blue: #1f86d4;
    --paper: #ffffff;
    --ink-light: #f2f2f2;
    --ink-dark: #1c1c1e;
  }
  * { margin: 0; padding: 0; box-sizing: border-box; }
  html, body {
    width: 1200px; height: 948px; overflow: hidden;
    background: var(--backdrop);
    font-family: "Montserrat", sans-serif;
  }
  .canvas { position: relative; width: 1200px; height: 948px; }
  .card {
    position: absolute; left: 280px; width: 640px; height: 366px;
    border-radius: 22px; overflow: hidden;
    background: var(--card-dark);
    border-bottom: 5px solid var(--card-edge);
    box-shadow: 0 18px 40px rgba(0,0,0,.45);
  }
  .card--front { top: 70px; }
  .card--back { top: 512px; }

  .wordmark {
    color: var(--brand-blue); font-weight: 800; letter-spacing: 2px;
    display: flex; align-items: center; gap: 14px; white-space: nowrap;
  }
  .wordmark__dot { width: 22px; height: 22px; border-radius: 50%; background: var(--brand-blue); flex: none; }
  .card--front .wordmark { position: absolute; inset: 0; justify-content: center; font-size: 40px; }

  .card--back .wordmark {
    position: absolute; left: 40px; top: 52px; font-size: 20px; gap: 10px; letter-spacing: 1px;
  }
  .card--back .wordmark__dot { width: 13px; height: 13px; }

  .back__panel {
    position: absolute; top: 0; right: 0; width: 300px; height: 100%;
    background: var(--paper);
    clip-path: polygon(22% 0, 100% 0, 100% 100%, 0 100%);
  }
  .back__arc { position: absolute; left: 0; bottom: 0; }
  .back__name { position: absolute; left: 92px; top: 118px; }
  .person__name {
    color: var(--brand-blue); font-weight: 700; font-size: 22px; letter-spacing: 1px;
    border-bottom: 2px solid var(--brand-blue); padding-bottom: 4px; white-space: nowrap;
  }
  .person__role {
    color: var(--ink-dark); font-weight: 500; font-size: 12px; letter-spacing: 2px;
    margin-top: 6px; text-align: right;
  }

  .contact {
    position: absolute; left: 40px; top: 140px; color: var(--ink-light);
    font-size: 14px; font-weight: 500; line-height: 1.55; list-style: none;
  }
  .contact__address { margin-bottom: 12px; }
  .contact__rule { width: 14px; height: 2px; background: var(--brand-blue); margin-bottom: 10px; }
  .contact__item { display: flex; align-items: center; gap: 10px; white-space: nowrap; }
  .contact__item svg { width: 13px; height: 13px; flex: none; }
  .icon-fill { fill: var(--brand-blue); }
  .icon-line { fill: none; stroke: var(--brand-blue); stroke-width: 2; }
</style>
</head>
<body>
<main class="canvas">
  <section class="card card--front">
    <div class="wordmark"><span class="wordmark__dot"></span>FERRIS CONTRACTING</div>
  </section>

  <section class="card card--back">
    <div class="wordmark"><span class="wordmark__dot"></span>FERRIS CONTRACTING</div>
    <ul class="contact">
      <li class="contact__address">204 Maple Court,<br>Suite 300, Dayton, OH 45402</li>
      <li class="contact__rule"></li>
      <li class="contact__item">
        <svg viewBox="0 0 24 24"><path class="icon-fill" d="M6.6 10.8a15 15 0 0 0 6.6 6.6l2.2-2.2c.3-.3.7-.4 1-.2 1.1.4 2.3.6 3.6.6.6 0 1 .4 1 1V20c0 .6-.4 1-1 1A17 17 0 0 1 3 4c0-.6.4-1 1-1h3.5c.6 0 1 .4 1 1 0 1.3.2 2.5.6 3.6.1.3 0 .7-.2 1z"/></svg>
        +1 555 0142 7788
      </li>
      <li class="contact__item">
        <svg viewBox="0 0 24 24"><path class="icon-line" d="M2 5h20v14H2z M2 5l10 8 10-8"/></svg>
        ferriscontracting@mailbox.com
      </li>
      <li class="contact__item">
        <svg viewBox="0 0 24 24"><circle class="icon-line" cx="12" cy="12" r="9"/><path class="icon-line" d="M3 12h18M12 3c3 3 3 15 0 18M12 3c-3 3-3 15 0 18"/></svg>
        www.ferriscontracting.com
      </li>
    </ul>
    <div class="back__panel">
      <svg class="back__arc" width="300" height="366" viewBox="0 0 300 366" aria-hidden="true">
        <path d="M40 300 Q170 250 300 190" fill="none" stroke="#1f86d4" stroke-width="22"/>
      </svg>
      <div class="back__name">
        <div class="person__name">OWEN FERRIS</div>
        <div class="person__role">MANAGER</div>
      </div>
    </div>
  </section>
</main>
</body>
</html>
```